Comparative Infographic

Prepare a comparison infographic for each of our (5) flavors of Coffee, the comparison is to compare the specific attributes of our products against other brands. please review our packaging and website to establish a feel for our branding. attached is the data and concept format, the format is just for informational purposes, developer should apply their own creative approach

```html
<!DOCTYPE html>
<html lang="en">
<head>
<meta charset="utf-8">
<title>Ember &amp; Rise vs Other – Flavor Comparison</title>
<link rel="stylesheet" href="https://fonts.googleapis.com/css2?family=Quicksand:wght@500;600;700&display=swap">
<style>
:root{
  --green:#1ed69c;
  --teal:#139f86;
  --deep:#1c3a40;
  --ink:#111;
  --paper:#fff;
}
*{box-sizing:border-box;margin:0;padding:0}
html,body{width:1200px;height:1200px;overflow:hidden;background:var(--paper)}
body{position:relative;font-family:"Quicksand",sans-serif;color:var(--ink)}
.sprites{position:absolute;width:0;height:0}

.card{position:absolute;border:6px solid transparent;border-radius:18px;
  background:linear-gradient(var(--paper),var(--paper)) padding-box,
             linear-gradient(160deg,var(--green) 0%,var(--green) 45%,var(--teal) 70%,var(--deep) 100%) border-box;
  box-shadow:2px 3px 4px rgba(0,0,0,.25);
  padding:12px 10px 8px 6px}
.flavor-1{left:156px;top:88px;width:397px;height:294px}
.flavor-2{left:780px;top:88px;width:397px;height:294px}
.flavor-3{left:156px;top:476px;width:397px;height:294px}
.flavor-4{left:780px;top:476px;width:397px;height:294px}
.flavor-5{left:459px;top:848px;width:427px;height:214px;padding:12px 12px 8px 8px}

.tab{position:absolute;left:-30px;top:-45px;height:56px;display:flex;align-items:center}
.tab-badge{width:56px;height:56px;border-radius:50%;background:var(--paper);
  border:6px solid var(--green);box-shadow:inset 0 0 0 3px var(--deep);
  display:flex;align-items:center;justify-content:center;
  font-weight:700;font-size:14px;color:var(--green);position:relative;z-index:2}
.tab-pill{margin-left:-8px;height:32px;padding:0 20px 0 24px;background:var(--paper);
  border:3px solid var(--green);border-radius:0 16px 16px 0;border-left:none;
  box-shadow:2px 2px 3px rgba(0,0,0,.2);
  font-weight:700;font-size:15px;display:flex;align-items:center;gap:16px}

.grid{display:grid;grid-template-columns:146px repeat(4,52px);align-items:end}
.flavor-5 .grid{grid-template-columns:160px repeat(4,57px)}
.head{height:18px;margin-left:12px}
.flavor-title{font-weight:700;font-size:14px;white-space:nowrap;margin-left:8px}
.brand{font-size:6.5px;font-weight:700;text-align:center;display:flex;align-items:center;justify-content:center;gap:2px;letter-spacing:.2px;color:var(--deep)}
.brand::before{content:"";width:7px;height:7px;border-radius:50%;border:1px solid currentColor;flex:none}
.brand.own{color:var(--teal)}

.row{height:22px;border-bottom:1px solid #222;margin-left:4px}
.flavor-5 .row{height:24px}
.label{font-size:12.5px;font-weight:500;padding-left:2px;padding-bottom:1px;white-space:nowrap}
.flavor-5 .label{font-size:13px}
.cell{text-align:center;font-weight:700;font-size:15.5px;line-height:20px;height:20px}
.cell svg{width:12px;height:12px;vertical-align:middle}
.cell .tick{width:14px;height:14px}

.notes{margin-top:6px;padding-left:10px;font-size:10px;font-weight:500;line-height:12px}
</style>
</head>
<body>

<svg class="sprites" aria-hidden="true">
  <symbol id="tick" viewBox="0 0 14 14"><path d="M1.5 7.5 L5 12 L12.5 1.5" fill="none" stroke="#111" stroke-width="2" stroke-linecap="round" stroke-linejoin="round"/></symbol>
  <symbol id="cross" viewBox="0 0 12 12"><path d="M2 2 L10 10 M10 2 L2 10" fill="none" stroke="#111" stroke-width="1.6" stroke-linecap="round"/></symbol>
</svg>

<!-- Keto-Cream & Sugar -->
<section class="card flavor-1">
  <div class="tab"><div class="tab-badge">E&amp;R</div><div class="tab-pill"><span>Vs</span><span>Other</span></div></div>
  <div class="grid head"><span class="flavor-title">Keto-Cream &amp; Sugar</span><span class="brand own">E&amp;R</span><span class="brand">HARBOR</span><span class="brand">RIDGELINE</span><span class="brand">MIDNIGHT</span></div>
  <div class="grid row"><span class="label">Hemp Derived THC/CBD</span><span class="cell"><svg class="tick"><use href="#tick"/></svg></span><span class="cell"><svg><use href="#cross"/></svg></span><span class="cell"><svg><use href="#cross"/></svg></span><span class="cell"><svg><use href="#cross"/></svg></span></div>
  <div class="grid row"><span class="label">Nootropics</span><span class="cell"><svg class="tick"><use href="#tick"/></svg></span><span class="cell"><svg><use href="#cross"/></svg></span><span class="cell"><svg><use href="#cross"/></svg></span><span class="cell"><svg><use href="#cross"/></svg></span></div>
  <div class="grid row"><span class="label">Adaptogens</span><span class="cell"><svg class="tick"><use href="#tick"/></svg></span><span class="cell"><svg><use href="#cross"/></svg></span><span class="cell"><svg><use href="#cross"/></svg></span><span class="cell"><svg><use href="#cross"/></svg></span></div>
  <div class="grid row"><span class="label">Energy Booster</span><span class="cell"><svg class="tick"><use href="#tick"/></svg></span><span class="cell"><svg><use href="#cross"/></svg></span><span class="cell"><svg><use href="#cross"/></svg></span><span class="cell"><svg><use href="#cross"/></svg></span></div>
  <div class="grid row"><span class="label">Collagen Protein</span><span class="cell">15</span><span class="cell">0</span><span class="cell">7</span><span class="cell">0</span></div>
  <div class="grid row"><span class="label">Vitamins B6 &amp; B12</span><span class="cell"><svg class="tick"><use href="#tick"/></svg></span><span class="cell"><svg><use href="#cross"/></svg></span><span class="cell"><svg><use href="#cross"/></svg></span><span class="cell"><svg><use href="#cross"/></svg></span></div>
  <div class="grid row"><span class="label">Healthy Fats</span><span class="cell"><svg class="tick"><use href="#tick"/></svg></span><span class="cell"><svg><use href="#cross"/></svg></span><span class="cell"><svg><use href="#cross"/></svg></span><span class="cell"><svg><use href="#cross"/></svg></span></div>
  <div class="grid row"><span class="label">Electrolytes</span><span class="cell"><svg class="tick"><use href="#tick"/></svg></span><span class="cell"><svg><use href="#cross"/></svg></span><span class="cell"><svg><use href="#cross"/></svg></span><span class="cell"><svg><use href="#cross"/></svg></span></div>
  <div class="grid row"><span class="label">Added Sugar</span><span class="cell">4g</span><span class="cell">25g</span><span class="cell">14g</span><span class="cell">14g**</span></div>
  <div class="grid row"><span class="label">Calories</span><span class="cell">120*</span><span class="cell">150</span><span class="cell">170</span><span class="cell">150**</span></div>
  <p class="notes">* 85 calories derived from Healthy Fats (MCT) and Collagen Protein.<br>**Calories may vary based upon specific taste preference.</p>
</section>

<!-- Café Mocha -->
<section class="card flavor-2">
  <div class="tab"><div class="tab-badge">E&amp;R</div><div class="tab-pill"><span>Vs</span><span>Other</span></div></div>
  <div class="grid head"><span class="flavor-title">Café Mocha</span><span class="brand own">E&amp;R</span><span class="brand">HARBOR</span><span class="brand">RIDGELINE</span><span class="brand">MIDNIGHT</span></div>
  <div class="grid row"><span class="label">Hemp Derived THC/CBD</span><span class="cell"><svg class="tick"><use href="#tick"/></svg></span><span class="cell"><svg><use href="#cross"/></svg></span><span class="cell"><svg><use href="#cross"/></svg></span><span class="cell"><svg><use href="#cross"/></svg></span></div>
  <div class="grid row"><span class="label">Nootropics</span><span class="cell"><svg class="tick"><use href="#tick"/></svg></span><span class="cell"><svg><use href="#cross"/></svg></span><span class="cell"><svg><use href="#cross"/></svg></span><span class="cell"><svg><use href="#cross"/></svg></span></div>
  <div class="grid row"><span class="label">Adaptogens</span><span class="cell"><svg class="tick"><use href="#tick"/></svg></span><span class="cell"><svg><use href="#cross"/></svg></span><span class="cell"><svg><use href="#cross"/></svg></span><span class="cell"><svg><use href="#cross"/></svg></span></div>
  <div class="grid row"><span class="label">Energy Booster</span><span class="cell"><svg class="tick"><use href="#tick"/></svg></span><span class="cell"><svg><use href="#cross"/></svg></span><span class="cell"><svg><use href="#cross"/></svg></span><span class="cell"><svg><use href="#cross"/></svg></span></div>
  <div class="grid row"><span class="label">Collagen Protein</span><span class="cell">15</span><span class="cell"><svg><use href="#cross"/></svg></span><span class="cell">7</span><span class="cell">0</span></div>
  <div class="grid row"><span class="label">Vitamins B6 &amp; B12</span><span class="cell"><svg class="tick"><use href="#tick"/></svg></span><span class="cell"><svg><use href="#cross"/></svg></span><span class="cell"><svg><use href="#cross"/></svg></span><span class="cell"><svg><use href="#cross"/></svg></span></div>
  <div class="grid row"><span class="label">Healthy Fats</span><span class="cell"><svg class="tick"><use href="#tick"/></svg></span><span class="cell"><svg><use href="#cross"/></svg></span><span class="cell"><svg><use href="#cross"/></svg></span><span class="cell"><svg><use href="#cross"/></svg></span></div>
  <div class="grid row"><span class="label">Electrolytes</span><span class="cell"><svg class="tick"><use href="#tick"/></svg></span><span class="cell"><svg><use href="#cross"/></svg></span><span class="cell"><svg><use href="#cross"/></svg></span><span class="cell"><svg><use href="#cross"/></svg></span></div>
  <div class="grid row"><span class="label">Added Sugar</span><span class="cell">0g</span><span class="cell">44g</span><span class="cell">14g</span><span class="cell">14g**</span></div>
  <div class="grid row"><span class="label">Calories</span><span class="cell">110*</span><span class="cell">440</span><span class="cell">170</span><span class="cell">150**</span></div>
  <p class="notes">* 85 calories derived from Healthy Fats (MCT) and Collagen Protein.<br>**Calories may vary based upon specific taste preference.</p>
</section>

<!-- Salted Caramel -->
<section class="card flavor-3">
  <div class="tab"><div class="tab-badge">E&amp;R</div><div class="tab-pill"><span>Vs</span><span>Other</span></div></div>
  <div class="grid head"><span class="flavor-title">Salted Caramel</span><span class="brand own">E&amp;R</span><span class="brand">HARBOR</span><span class="brand">RIDGELINE</span><span class="brand">MIDNIGHT</span></div>
  <div class="grid row"><span class="label">Hemp Derived THC/CBD</span><span class="cell"><svg class="tick"><use href="#tick"/></svg></span><span class="cell"><svg><use href="#cross"/></svg></span><span class="cell"><svg><use href="#cross"/></svg></span><span class="cell"><svg><use href="#cross"/></svg></span></div>
  <div class="grid row"><span class="label">Nootropics</span><span class="cell"><svg class="tick"><use href="#tick"/></svg></span><span class="cell"><svg><use href="#cross"/></svg></span><span class="cell"><svg><use href="#cross"/></svg></span><span class="cell"><svg><use href="#cross"/></svg></span></div>
  <div class="grid row"><span class="label">Adaptogens</span><span class="cell"><svg class="tick"><use href="#tick"/></svg></span><span class="cell"><svg><use href="#cross"/></svg></span><span class="cell"><svg><use href="#cross"/></svg></span><span class="cell"><svg><use href="#cross"/></svg></span></div>
  <div class="grid row"><span class="label">Energy Booster</span><span class="cell"><svg class="tick"><use href="#tick"/></svg></span><span class="cell"><svg><use href="#cross"/></svg></span><span class="cell"><svg><use href="#cross"/></svg></span><span class="cell"><svg><use href="#cross"/></svg></span></div>
  <div class="grid row"><span class="label">Collagen Protein</span><span class="cell">15</span><span class="cell"><svg><use href="#cross"/></svg></span><span class="cell">7</span><span class="cell">0</span></div>
  <div class="grid row"><span class="label">Vitamins B6 &amp; B12</span><span class="cell"><svg class="tick"><use href="#tick"/></svg></span><span class="cell"><svg><use href="#cross"/></svg></span><span class="cell"><svg><use href="#cross"/></svg></span><span class="cell"><svg><use href="#cross"/></svg></span></div>
  <div class="grid row"><span class="label">Healthy Fats</span><span class="cell"><svg class="tick"><use href="#tick"/></svg></span><span class="cell"><svg><use href="#cross"/></svg></span><span class="cell"><svg><use href="#cross"/></svg></span><span class="cell"><svg><use href="#cross"/></svg></span></div>
  <div class="grid row"><span class="label">Electrolytes</span><span class="cell"><svg class="tick"><use href="#tick"/></svg></span><span class="cell"><svg><use href="#cross"/></svg></span><span class="cell"><svg><use href="#cross"/></svg></span><span class="cell"><svg><use href="#cross"/></svg></span></div>
  <div class="grid row"><span class="label">Added Sugar</span><span class="cell">0g</span><span class="cell">50g</span><span class="cell">14g</span><span class="cell">0g</span></div>
  <div class="grid row"><span class="label">Calories</span><span class="cell">110*</span><span class="cell">480</span><span class="cell">170</span><span class="cell">150**</span></div>
  <p class="notes">* 85 calories derived from Healthy Fats (MCT) and Collagen Protein.<br>**Calories may vary based upon specific taste preference.</p>
</section>

<!-- Vanilla Latte -->
<section class="card flavor-4">
  <div class="tab"><div class="tab-badge">E&amp;R</div><div class="tab-pill"><span>Vs</span><span>Other</span></div></div>
  <div class="grid head"><span class="flavor-title">Vanilla Latte</span><span class="brand own">E&amp;R</span><span class="brand">HARBOR</span><span class="brand">RIDGELINE</span><span class="brand">MIDNIGHT</span></div>
  <div class="grid row"><span class="label">Hemp Derived THC/CBD</span><span class="cell"><svg class="tick"><use href="#tick"/></svg></span><span class="cell"><svg><use href="#cross"/></svg></span><span class="cell"><svg><use href="#cross"/></svg></span><span class="cell"><svg><use href="#cross"/></svg></span></div>
  <div class="grid row"><span class="label">Nootropics</span><span class="cell"><svg class="tick"><use href="#tick"/></svg></span><span class="cell"><svg><use href="#cross"/></svg></span><span class="cell"><svg><use href="#cross"/></svg></span><span class="cell"><svg><use href="#cross"/></svg></span></div>
  <div class="grid row"><span class="label">Adaptogens</span><span class="cell"><svg class="tick"><use href="#tick"/></svg></span><span class="cell"><svg><use href="#cross"/></svg></span><span class="cell"><svg><use href="#cross"/></svg></span><span class="cell"><svg><use href="#cross"/></svg></span></div>
  <div class="grid row"><span class="label">Energy Booster</span><span class="cell"><svg class="tick"><use href="#tick"/></svg></span><span class="cell"><svg><use href="#cross"/></svg></span><span class="cell"><svg><use href="#cross"/></svg></span><span class="cell"><svg><use href="#cross"/></svg></span></div>
  <div class="grid row"><span class="label">Collagen Protein</span><span class="cell">15</span><span class="cell"><svg><use href="#cross"/></svg></span><span class="cell">7</span><span class="cell">0</span></div>
  <div class="grid row"><span class="label">Vitamins B6 &amp; B12</span><span class="cell"><svg class="tick"><use href="#tick"/></svg></span><span class="cell"><svg><use href="#cross"/></svg></span><span class="cell"><svg><use href="#cross"/></svg></span><span class="cell"><svg><use href="#cross"/></svg></span></div>
  <div class="grid row"><span class="label">Healthy Fats</span><span class="cell"><svg class="tick"><use href="#tick"/></svg></span><span class="cell"><svg><use href="#cross"/></svg></span><span class="cell"><svg><use href="#cross"/></svg></span><span class="cell"><svg><use href="#cross"/></svg></span></div>
  <div class="grid row"><span class="label">Electrolytes</span><span class="cell"><svg class="tick"><use href="#tick"/></svg></span><span class="cell"><svg><use href="#cross"/></svg></span><span class="cell"><svg><use href="#cross"/></svg></span><span class="cell"><svg><use href="#cross"/></svg></span></div>
  <div class="grid row"><span class="label">Added Sugar</span><span class="cell">0g</span><span class="cell">25g</span><span class="cell">14g</span><span class="cell">14g**</span></div>
  <div class="grid row"><span class="label">Calories</span><span class="cell">110*</span><span class="cell">320</span><span class="cell">170</span><span class="cell">150**</span></div>
  <p class="notes">* 85 calories derived from Healthy Fats (MCT) and Collagen Protein.<br>**Calories may vary based upon specific taste preference.</p>
</section>

<!-- Classic Black -->
<section class="card flavor-5">
  <div class="tab"><div class="tab-badge">E&amp;R</div><div class="tab-pill"><span>Vs</span><span>Other</span></div></div>
  <div class="grid head"><span class="flavor-title">Classic Black</span><span class="brand own">E&amp;R</span><span class="brand">HARBOR</span><span class="brand">RIDGELINE</span><span class="brand">MIDNIGHT</span></div>
  <div class="grid row"><span class="label">Hemp Derived THC/CBD</span><span class="cell"><svg class="tick"><use href="#tick"/></svg></span><span class="cell"><svg><use href="#cross"/></svg></span><span class="cell"><svg><use href="#cross"/></svg></span><span class="cell"><svg><use href="#cross"/></svg></span></div>
  <div class="grid row"><span class="label">Nootropics</span><span class="cell"><svg class="tick"><use href="#tick"/></svg></span><span class="cell"><svg><use href="#cross"/></svg></span><span class="cell"><svg><use href="#cross"/></svg></span><span class="cell"><svg><use href="#cross"/></svg></span></div>
  <div class="grid row"><span class="label">Adaptogens</span><span class="cell"><svg class="tick"><use href="#tick"/></svg></span><span class="cell"><svg><use href="#cross"/></svg></span><span class="cell"><svg><use href="#cross"/></svg></span><span class="cell"><svg><use href="#cross"/></svg></span></div>
  <div class="grid row"><span class="label">Energy Booster</span><span class="cell"><svg class="tick"><use href="#tick"/></svg></span><span class="cell"><svg><use href="#cross"/></svg></span><span class="cell"><svg><use href="#cross"/></svg></span><span class="cell"><svg><use href="#cross"/></svg></span></div>
  <div class="grid row"><span class="label">Collagen Protein</span><span class="cell"><svg class="tick"><use href="#tick"/></svg></span><span class="cell"><svg><use href="#cross"/></svg></span><span class="cell"><svg><use href="#cross"/></svg></span><span class="cell"><svg><use href="#cross"/></svg></span></div>
  <div class="grid row"><span class="label">Vitamins B6 &amp; B12</span><span class="cell"><svg class="tick"><use href="#tick"/></svg></span><span class="cell"><svg><use href="#cross"/></svg></span><span class="cell"><svg><use href="#cross"/></svg></span><span class="cell"><svg><use href="#cross"/></svg></span></div>
  <div class="grid row"><span class="label">Healthy Fats</span><span class="cell"><svg class="tick"><use href="#tick"/></svg></span><span class="cell"><svg><use href="#cross"/></svg></span><span class="cell"><svg><use href="#cross"/></svg></span><span class="cell"><svg><use href="#cross"/></svg></span></div>
</section>

</body>
</html>
```